TIVARELCAP web-presence redisign

We would like to have our existing web-presence redesigned. Have a look at www.tivarel.ch (please use explorer). To the existing 11 pages we would add one more.

```html
<!DOCTYPE html>
<html lang="de">
<head>
<meta charset="utf-8">
<title>TIVARELCAP Zahnarztpraxis</title>
<link href="https://fonts.googleapis.com/css2?family=Open+Sans:wght@400;600&family=Cinzel&family=Tinos&display=swap" rel="stylesheet">
<style>
:root{
  --navy:#0b0b52;
  --header:#cbcbcb;
  --orange:#f39a2b;
  --gold:#e6b24b;
  --band:#e4e4e4;
  --light:#f1f1f1;
  --text:#333;
  --muted:#666;
  --footer:#2f2f2f;
  --link:#3ea3e2;
  --blue:#0f86c9;
}
*{margin:0;padding:0;box-sizing:border-box}
html,body{width:702px;height:1200px;overflow:hidden}
body{position:relative;font-family:"Open Sans",Arial,sans-serif;color:var(--text);background:#fff}
.abs{position:absolute}
.site-header{left:0;top:0;width:702px;height:86px;background:linear-gradient(#d2d2d2,#c2c2c2)}
.brand{left:66px;top:10px;display:flex;align-items:center;gap:8px}
.brand-mark{width:44px;height:44px;border-radius:50%;background:var(--gold)}
.brand-name{font-family:"Open Sans",sans-serif;font-size:24px;color:#fff;letter-spacing:1px}
.lang{top:13px;width:19px;height:12px;background:#888}
.search{left:478px;top:49px;width:130px;height:18px;background:#fff;border:1px solid #bbb;font-size:6px;font-style:italic;color:#777;padding:5px 6px}
.search-btn{left:608px;top:48px;width:24px;height:19px;background:var(--blue)}
.main-nav{left:0;top:86px;width:702px;height:32px;background:var(--navy);display:flex;padding-left:62px}
.main-nav a{color:#fff;font-size:9px;text-decoration:none;padding:0 21px;line-height:32px;border-right:1px solid #23236a}
.main-nav a.active{color:var(--orange)}
.main-nav a:last-child{border:none}
.hero{left:0;top:118px;width:702px;height:275px;background:linear-gradient(90deg,#cfe8f5,#a8d6ef 45%,#d9eef8)}
.hero-title{left:390px;top:170px;width:238px;height:19px;background:#fff;font-size:12.5px;text-align:center;line-height:19px;color:#111}
.hero-text{left:380px;top:204px;width:248px;font-size:8px;line-height:14px;text-align:right;color:#333}
.hero-btn{left:530px;top:290px;width:100px;height:32px;background:var(--navy);color:#fff;font-size:10px;font-weight:600;text-align:center;line-height:32px;border-radius:2px}
.arrow{top:241px;width:22px;height:24px;background:#111}
.services{left:0;top:393px;width:702px;height:207px;background:var(--light)}
.service{top:25px;width:130px;text-align:center}
.service h3{font-size:11px;font-weight:600;margin:14px 0 10px;color:#111}
.service p{font-size:7.2px;line-height:10.5px;color:#444;height:48px}
.service .more{display:inline-block;margin-top:6px;width:70px;height:22px;background:var(--navy);color:#fff;font-size:8px;line-height:22px;border:1px solid #7b7bb0}
.welcome{left:0;top:600px;width:702px;height:87px;background:var(--band);text-align:center}
.welcome h2{font-weight:400;font-size:13.5px;margin-top:12px;color:#222}
.welcome p{font-size:11.5px;line-height:18px;color:#666;margin:8px auto 0;width:540px}
.feature{top:711px;width:189px;height:139px}
.feature .photo{height:116px}
.feature .caption{height:23px;background:var(--gold);display:flex;justify-content:space-between;align-items:center;padding:0 4px 0 8px;font-size:10.5px;color:#333}
.feature .view{width:50px;height:15px;background:#fff;border-radius:8px;font-size:8px;text-align:center;line-height:15px}
.team-title{left:57px;top:876px;width:587px;height:18px;display:flex;align-items:center;gap:10px;font-size:13.5px}
.team-title span.line{flex:1;height:1px;background:var(--gold)}
.team{left:0;top:901px;width:702px;height:161px;background:var(--band)}
.member{top:12px;width:120px;text-align:center;font-size:8.3px;line-height:17px;color:#222}
.member .avatar{width:94px;height:94px;border-radius:50%;margin:0 auto 10px;background:radial-gradient(circle at 50% 40%,#e8c6aa,#8a6a52)}
.footer{left:0;top:1062px;width:702px;height:138px;background:radial-gradient(ellipse at 50% 0,#444,var(--footer) 70%)}
.footer h4{font-weight:400;font-size:11px;color:var(--link)}
.contact-line{display:flex;gap:8px;align-items:flex-start;font-size:7.5px;color:#ddd;line-height:11px}
.social{top:1082px;width:15px;height:15px}
.legal{right:74px;top:1108px;text-align:right;font-size:7px;line-height:14px;color:#ddd}
</style>
</head>
<body>
<header class="site-header abs">
  <div class="brand abs"><span class="brand-mark"></span><span class="brand-name">TIVARELCAP</span></div>
  <span class="lang abs" style="left:585px"></span>
  <span class="lang abs" style="left:609px;background:#555"></span>
  <div class="search abs">Enter Your Keyword...</div>
  <div class="search-btn abs"><svg width="24" height="19" viewBox="0 0 24 19"><circle cx="11" cy="9" r="4" fill="none" stroke="#fff" stroke-width="2"/><line x1="14" y1="12" x2="17" y2="15" stroke="#fff" stroke-width="2"/></svg></div>
</header>
<nav class="main-nav abs">
  <a class="active">Home</a><a>Zahnmedizin</a><a>Dentalhygiene</a><a>Team</a><a>Kontakt</a>
</nav>
<section class="hero abs" role="img" aria-label="Lächelnde Frau mit Händen am Kinn vor hellblauem Wasserhintergrund"></section>
<div class="hero-title abs">Vestibulum Dignissim Varius Suscipit</div>
<p class="hero-text abs">Cum sociis natoque penatibus et magnis dis parturient montes, nascetur ridiculus mus. In iaculis facilisis massa. Etiam eu urna. Cum sociis natoque penatibus et magnis dis parturient montes, nascetur ridiculus mus. In iaculis facilisis massa. Etiam eu urna.</p>
<div class="hero-btn abs">Learn More</div>
<div class="arrow abs" style="left:0"><svg width="22" height="24"><polyline points="14,6 8,12 14,18" fill="none" stroke="#fff"/></svg></div>
<div class="arrow abs" style="left:680px"><svg width="22" height="24"><polyline points="8,6 14,12 8,18" fill="none" stroke="#fff"/></svg></div>

<section class="services abs">
  <div class="service abs" style="left:69px">
    <svg width="40" height="44" viewBox="0 0 40 44"><path d="M8 6c6-4 10 0 12 0s6-4 12 0c4 4 2 12 0 18-2 8-2 18-6 18-3 0-3-12-6-12s-3 12-6 12c-4 0-4-10-6-18-2-6-4-14 0-18z" fill="#ddd" stroke="#888"/></svg>
    <h3>Zahnarztbehandlung</h3>
    <p>Durch eine sanfte zahnmedizinische Behandlungsmethode soll dem Patienten eine angstfreie Behandlung ermöglicht werden.</p>
    <span class="more">More &gt;&gt;</span>
  </div>
  <div class="service abs" style="left:212px">
    <svg width="40" height="44" viewBox="0 0 40 44"><path d="M15 6h10v11h11v10H25v11H15V27H4V17h11z" fill="#666"/></svg>
    <h3>Notfälle</h3>
    <p>Notfälle sind in einer Zahnarztpraxis etwas Alltägliches. Aus diesem Grund haben wir für jeden Tag Zeitreserven eingeplant.....</p>
    <span class="more">More &gt;&gt;</span>
  </div>
  <div class="service abs" style="left:358px">
    <svg width="40" height="44" viewBox="0 0 40 44"><path d="M8 8c6-4 10 0 12 0s6-4 12 0c4 4 2 12 0 17-2 7-3 15-6 15-3 0-3-10-6-10s-3 10-6 10c-3 0-4-8-6-15-2-5-4-13 0-17z" fill="#e2e2e2" stroke="#999"/></svg>
    <h3>Dentalhygiene</h3>
    <p>Zur modernen Zahnmedizin gehört die Dentalhygiene, welche den Erhalt der eigenen Zähne verlängert.</p>
    <span class="more">More &gt;&gt;</span>
  </div>
  <div class="service abs" style="left:508px">
    <svg width="40" height="44" viewBox="0 0 40 44"><path d="M8 4v14c0 8 12 8 12 0V4M14 26v6c0 8 16 8 16 0v-8" fill="none" stroke="#555" stroke-width="2"/><circle cx="30" cy="20" r="4" fill="#ccc" stroke="#555" stroke-width="2"/></svg>
    <h3>Gesundheit</h3>
    <p>Schöne und gesunde Zähne sind für das äussere Erscheinungsbild und die allgemeine Gesundheit von grosser Bedeutung.</p>
    <span class="more">More &gt;&gt;</span>
  </div>
</section>

<section class="welcome abs">
  <h2>HERZLICH WILLKOMMEN IN UNSERER NEUEN PRAXIS.</h2>
  <p>Es ist unser Ziel, Ihr Wohlbefinden zu steigern. Sie sollen die Schönheit des Alltags mit gesunden Zähnen geniessen und in jeder Situation herzhaft lachen können.</p>
</section>

<div class="feature abs" style="left:57px">
  <div class="photo" role="img" aria-label="Zahnarzt behandelt Patientin mit Assistentin" style="background:linear-gradient(135deg,#e9e4dc,#b9b3aa)"></div>
  <div class="caption">Zahnarztbehandlung<span class="view">View</span></div>
</div>
<div class="feature abs" style="left:255px">
  <div class="photo" role="img" aria-label="Zahnarzt mit Mundschutz und Instrumenten" style="background:linear-gradient(135deg,#d8e2ea,#aab8c4)"></div>
  <div class="caption">Kompetenzen<span class="view">View</span></div>
</div>
<div class="feature abs" style="left:455px">
  <div class="photo" role="img" aria-label="Patientin bei der Dentalhygiene" style="background:linear-gradient(135deg,#6f9fd6,#d7c3b5)"></div>
  <div class="caption">Dentalhygiene<span class="view">View</span></div>
</div>

<div class="team-title abs"><span class="line"></span>TEAM<span class="line"></span></div>
<section class="team abs">
  <div class="member abs" style="left:66px"><div class="avatar" role="img" aria-label="Porträt Zahnärztin"></div>Dr. med. dent.<br>Laura Berger</div>
  <div class="member abs" style="left:182px"><div class="avatar" role="img" aria-label="Porträt Dentalassistentin"></div>Sofia Marchetti<br>Dentalassistentin</div>
  <div class="member abs" style="left:298px"><div class="avatar" role="img" aria-label="Porträt Dentalassistentin in Ausbildung"></div>Nadine Keller<br>Dentalassistentin i.A.</div>
  <div class="member abs" style="left:410px"><div class="avatar" role="img" aria-label="Porträt Dentalassistentin in Ausbildung"></div>Lena Hofmann<br>Dentalassistentin i.A.</div>
  <div class="member abs" style="left:525px"><div class="avatar" role="img" aria-label="Porträt Zahnärztin"></div>Dr. med. dent.<br>Petra Amsler</div>
</section>

<footer class="footer abs">
  <h4 class="abs" style="left:59px;top:14px">Contact Info</h4>
  <div class="contact-line abs" style="left:59px;top:37px"><svg width="11" height="11"><path d="M1 6L5.5 1 10 6v5H1z" fill="#aaa"/></svg><span>Lindenweg 12<br>CH-8400 Musterdorf</span></div>
  <div class="contact-line abs" style="left:59px;top:72px"><svg width="12" height="10"><path d="M1 3c3-3 7-3 10 0l-2 2-2-1H5L3 5z M3 6h6v4H3z" fill="#aaa"/></svg><span>+41 (0)44 555 01 23</span></div>
  <div class="contact-line abs" style="left:59px;top:97px"><svg width="12" height="9"><rect x="0.5" y="0.5" width="11" height="8" fill="#aaa"/><polyline points="1,1 6,5 11,1" fill="none" stroke="#555"/></svg><span>info@tivarel.ch</span></div>
  <h4 class="abs" style="left:243px;top:24px">Newsletter</h4>
  <div class="abs" style="left:244px;top:41px;width:151px;height:19px;background:#fff;border-radius:2px;font-size:6px;font-style:italic;color:#777;padding:6px">Your Email Id</div>
  <div class="abs" style="left:333px;top:74px;width:61px;height:18px;background:var(--blue);color:#fff;font-size:9px;text-align:center;line-height:18px">Subscribe</div>
  <div class="legal abs" style="top:46px">Privacy Policy &nbsp;|&nbsp; Terms<br>© 2014 TIVARELCAP | Dr. med. dent. M. Brunner-Aebi.<br>All rights reserved<br>X2</div>
</footer>
<span class="social abs" style="left:500px;background:#3b5a9a"></span>
<span class="social abs" style="left:523px;background:#3fa9e0"></span>
<span class="social abs" style="left:545px;background:#444;border:1px solid #777"></span>
<span class="social abs" style="left:567px;background:#e8902c"></span>
<span class="social abs" style="left:590px;background:#c9262c"></span>
<span class="social abs" style="left:613px;background:#7f97a8"></span>
</body>
</html>
```